3 Posters for House Designer

I'm installing a set of 3 posters on our office wall to describe the benefits of our house design services. These posters are A0 size and will be seen from the front windows of the office. I have already purchased the AO snap frames to hold the posters, they are silver in colour.

We, Farlow Studio, design houses. We offer Architectural services but as we didn't study Architecture, we're not permitted to use the word Architect or any derivative there of. So no words allowed that say Architect, Architecture or Architectural and the like.

Each poster will highlight a benefit of engaging Farlow Studio to design a house and the posters will be lined up side by side.

The first benefit is GENUINE PASSION.
I am genuinely passionate about designing homes that fit my clients like a glove in every way. I genuinely care about my clients doing the right thing by themselves and I'm not a "yes man". I challenge myself and my clients to ensure the best possible result.

The second benefit is CREATIVE THINKING.
I love a challenge. I can spend hours, even days, working on one small aspect of a house design to make it work best. I love solving design problems on difficult sites. What I pride myself on is delivering house designs which are as great to live with as they are to look at; form and function, beautiful yet practical.

The third benefit is GUARANTEED RESULTS.
My genuine passion and creative thinking result in my initial house designs being 95% right, for my clients, the first time; requiring very few changes. This is why I offer, iron clad, guarantees which form part of our design contract. These guarantees include:
1. Our clients absolutely loving our design. If they want to change something, we'll change it at no additional cost; no matter how big the changes or how many.
2. We guarantee our house designs will be within the given budget to build the house. If not, we'll amend our design at no additional cost.
3. We guarantee our house designs will meet the required minimum 6 star energy efficiency rating. If not, we'll amend the design at no additional cost.
4. We guarantee Council approval to build as designed. If not, we'll amend our design at no additional cost.

I see each benefit title being the hero on each poster (ie GENUINE PASSION). I see white type on a light blue background. I see A hero shot of stylish houses in the backgrounds but blurred. I see life in the posters in the form of colour and happy people (customers). Our customers are aged between 40 & 60.

I have a logo (uploaded) and have already purchased images of people if required. Please advise if you want these.

Check out our website at www.farlow-studio.com.au/Kelmore

Target Market(s)

Couples aged 40 - 60

Industry/Entity Type

House

Requirements
Must have
• Stylish house images, happy people (couples & families), big, bold, hero titles at the top of each of the three posters.

```html
<!DOCTYPE html>
<html lang="en">
<head>
<meta charset="utf-8">
<title>Farlow Studio – Poster Series</title>
<link href="https://fonts.googleapis.com/css2?family=Roboto:wght@400;900&display=swap" rel="stylesheet">
<style>
  :root {
    --board: #808080;
    --white: #ffffff;
    --brand-blue: #2a7fc1;
    --brand-navy: #1d4f86;
    --tag-grey: #4a5a6a;
    --p1-top: #2a82cc;
    --p1-bottom: #c9e4f6;
    --p2-top: #4772bd;
    --p2-bottom: #eef3fa;
    --p3-top: #1a62b8;
    --p3-bottom: #9cc6ea;
  }
  html, body {
    margin: 0;
    width: 1200px;
    height: 985px;
    overflow: hidden;
    background: var(--board);
    font-family: "Roboto", Arial, sans-serif;
  }
  .board { position: relative; width: 1200px; height: 985px; }
  .poster {
    position: absolute;
    overflow: hidden;
    box-shadow: 2px 3px 6px rgba(0,0,0,.35);
  }
  .poster--passion  { left: 8px;   top: 200px; width: 382px; height: 536px;
    background: linear-gradient(180deg, var(--p1-top) 0%, #5aa6de 55%, var(--p1-bottom) 100%); }
  .poster--creative { left: 413px; top: 200px; width: 378px; height: 536px;
    background: linear-gradient(180deg, var(--p2-top) 0%, #8fb0dc 55%, var(--p2-bottom) 100%); }
  .poster--results  { left: 813px; top: 197px; width: 382px; height: 539px;
    background: linear-gradient(180deg, var(--p3-top) 0%, #5b9ad8 45%, var(--p3-bottom) 100%); }

  .photo { position: absolute; }
  .poster--passion .photo {
    left: 0; top: 200px; width: 382px; height: 336px;
    background: radial-gradient(ellipse 55% 45% at 65% 45%, #e9d6b8 0%, #d9b68f 35%, rgba(230,240,250,.6) 70%, rgba(230,240,250,0) 100%);
  }
  .poster--creative .photo {
    left: 0; top: 200px; width: 378px; height: 336px;
    background: radial-gradient(ellipse 45% 40% at 62% 35%, #3c4c66 0%, #7d8ca3 45%, rgba(238,243,250,.7) 75%, rgba(238,243,250,0) 100%);
  }
  .poster--results .photo {
    left: 0; top: 60px; width: 382px; height: 479px;
    background:
      radial-gradient(ellipse 40% 25% at 60% 22%, rgba(255,255,255,.9) 0%, rgba(255,255,255,0) 100%),
      radial-gradient(ellipse 40% 30% at 78% 85%, #3d7fc9 0%, #d9c24a 40%, rgba(180,205,230,0) 75%),
      linear-gradient(180deg, rgba(0,0,0,0) 0%, rgba(0,0,0,0) 45%, #c7d3de 55%, #9fb0c2 100%);
  }

  .hero-title {
    position: absolute;
    left: 0;
    top: 0;
    width: 100%;
    height: 100%;
    margin: 0;
    overflow: visible;
  }
  .hero-title text {
    font-family: "Roboto", Arial, sans-serif;
    font-weight: 900;
    font-size: 130px;
    fill: rgba(255,255,255,.93);
    filter: drop-shadow(-2px 2px 2px rgba(0,0,40,.4));
  }

  .brand {
    position: absolute;
    right: 14px;
    bottom: 16px;
    text-align: right;
  }
  .brand__name {
    font-size: 22px;
    font-weight: 400;
    color: var(--brand-blue);
    line-height: 1;
  }
  .poster--results .brand__name { color: var(--brand-navy); }
  .brand__tag {
    margin-top: 4px;
    font-size: 5.5px;
    letter-spacing: .4px;
    color: var(--tag-grey);
  }
</style>
</head>
<body>
<main class="board">
  <section class="poster poster--passion">
    <div class="photo" role="img" aria-label="A model house held in an open hand against a blue sky with clouds and faint plan lines"></div>
    <svg class="hero-title" viewBox="0 0 382 536" aria-label="Genuine Passion" role="heading" aria-level="2">
      <g transform="rotate(-90)">
        <text x="-525" y="100" textLength="510" lengthAdjust="spacingAndGlyphs">GENUINE</text>
        <text x="-525" y="197" textLength="510" lengthAdjust="spacingAndGlyphs">PASSION</text>
      </g>
    </svg>
    <div class="brand">
      <div class="brand__name">Farlow Studio</div>
      <div class="brand__tag">RESIDENTIAL DESIGNERS PERTH, WESTERN AUSTRALIA</div>
    </div>
  </section>

  <section class="poster poster--creative">
    <div class="photo" role="img" aria-label="A rendered house model with a dark roof sitting on floor plan drawings"></div>
    <svg class="hero-title" viewBox="0 0 378 536" aria-label="Creative Thinking" role="heading" aria-level="2">
      <g transform="rotate(-90)">
        <text x="-505" y="102" textLength="497" lengthAdjust="spacingAndGlyphs">CREATIVE</text>
        <text x="-505" y="197" textLength="497" lengthAdjust="spacingAndGlyphs">THINKING</text>
      </g>
    </svg>
    <div class="brand">
      <div class="brand__name">Farlow Studio</div>
      <div class="brand__tag">RESIDENTIAL DESIGNERS PERTH, WESTERN AUSTRALIA</div>
    </div>
  </section>

  <section class="poster poster--results">
    <div class="photo" role="img" aria-label="A happy family with outstretched arms in front of a white weatherboard house under a cloudy blue sky"></div>
    <svg class="hero-title" viewBox="0 0 382 539" aria-label="Guaranteed Results" role="heading" aria-level="2">
      <g transform="rotate(-90)">
        <text x="-528" y="99" textLength="515" lengthAdjust="spacingAndGlyphs">GUARANTEED</text>
        <text x="-528" y="199" textLength="515" lengthAdjust="spacingAndGlyphs">RESULTS</text>
      </g>
    </svg>
    <div class="brand">
      <div class="brand__name">Farlow Studio</div>
      <div class="brand__tag">RESIDENTIAL DESIGNERS PERTH, WESTERN AUSTRALIA</div>
    </div>
  </section>
</main>
</body>
</html>
```